Business Card Design for drone videography and photography

I have a Vorkel Skyra 3 drone. I am looking for a logo to somehow incorporate with my business name. I don't even know what is an appropriate font. I am most filming real estate homes. I want something simplistic and a logo that makes sense for the business that I'm in. xxxxxxxxxxxxxxxxxxxxxxxxxxxxxxxxxxxxxxxxxxxxxxxxxxxxxxxxxxxxxxxxxxxxxxxxxxxxxxxxxxxxxxxxxxxxxxxxxxxxxxxxxxxxxxxxxxxxxxxxxxxxxxxxxxxxxxxxxxxxxxxxxxxxxxxxxxxxxxxxxxxxxxxxxxxxxxxxxxxxxxxxxxxxxxxxxxxxxxxxxxxxxxxxxxxxxxxxxxxxxxxxxxxxxxxxxxxxxxxxxxxxxxxxxxxxxxxxxxxxxxxxxxxxxxxxxxxxxxxxxxxxxxxxxxxxxxxxxxxxxxxxxxxxxxxxxxxxxxxxxxxxxxxxxxxxxxxxxxxxxxxxxxxxxxxxxxxxxxxxxxxxxxxxxxxxxxxxxxxxxxxxxxxxxxxxxxxxxxxxxxxxxxxxxxxxxxxxxxxxxxxxxxxxxxxxxxxxxxxxxxxxxxxxxxxxxxxxxxxxxxxxxxxxxxxxxxxxxxxxxxxxxxxxxxxxxxxxxxxxxxxxxxxxxxxxxxxxxxxxxxxxxxxxxxxxxxxxxxxxxxxxxxxxxxxxxxxxxxxxxxxxxxxxxxxxxxxxxxxxxxxxxxxxxxxxxxxxxxxxxxxxxxxxxxxxxxxxxxxxxxxxxxxxxxxxxxxxxxxxxxxxxxxxxxxxxxxxxxxxxxxxxxxxxxxxxxxxxxxxxxxxxxxxxxxxxxxxxxxxxxxxxxxxxxxxxxxxxxxxxxxxxxxxxxxxxxxxxxxxxxxxxxxxxxxxxxxxxxxxxxxxxxxxxxxxxxxxxxxxxxxxxxxxxxxxxxxxxxxxxxxxxxxxxxxxxxxxxxxxxxxxxxxxxxxxxxxxxxxxxxxxxxxxxxxxxxxxxxxxxxxxxxxxxxxxxxxxxxxxxxxxxxxxxxxxxxxxxxxxxxxxxxxxxxxxxxxxxxxxxxxxxxxxxxxxxxxxxxxxxxxxxxxxxxxxxxxxxxxxxxxxxxxxxxxxxxxxxxxxxxxxxxxxxxxxxxxxxxxxxxxxxxxxxxxxxxxxxxxxxxxxxxxxxxxxxxxxxxxx

Target Market(s)

Real estate

Industry/Entity Type

Business

Contact Information for Business Card

TRASK AERIAL IMAGING
Daniel Trask
Owner/Operator

40528 Birchwood Ct.
Calloway Falls KS 67012

620-555-0187
dtrask@traskaerialimaging.com

NAB Drone Certified
Insured
Section 333 Exempt
Vexo Flight Class Certified

Font styles to use
Other font styles liked:
• PUMP DEMI BOLD LET

Requirements
Must have
• Maybe have the certifications on the back??? The business card must be more serious than playful
Nice to have
• Possibly have the logo work itself into the business name?
Should not have
• nothing that looks like a "fun" business. I want this business card to look professional but also simplistic. I don't want a picture that I took from my drone as the background.

```html
<!DOCTYPE html>
<html lang="en">
<head>
<meta charset="utf-8">
<title>Trask Aerial Imaging – Business Card</title>
<link rel="stylesheet" href="https://fonts.googleapis.com/css2?family=Audiowide&family=Michroma&family=Cormorant+Garamond:ital,wght@1,400&family=Kalam:wght@700&display=swap">
<style>
  :root {
    --page: #ecebe8;
    --card: #ffffff;
    --blue: #3d66b0;
    --blue-light: #6a8fd0;
    --ink: #0d0f1a;
    --white: #ffffff;
  }
  * { margin: 0; padding: 0; box-sizing: border-box; }
  html, body { width: 1200px; height: 1200px; overflow: hidden; }
  body {
    background: var(--page);
    position: relative;
    font-family: "Kalam", cursive;
  }
  .card {
    position: absolute;
    left: 250px;
    width: 700px;
    height: 400px;
    background: var(--card);
    overflow: hidden;
    box-shadow: 0 6px 22px rgba(0,0,0,.18);
  }
  .card--front { top: 130px; }
  .card--back  { top: 670px; }

  /* Front */
  .front-disc { position: absolute; inset: 0; }
  .brand {
    position: absolute;
    left: 40px;
    top: 222px;
    font-family: "Audiowide", sans-serif;
    color: var(--ink);
    line-height: 1;
  }
  .brand__name { font-size: 66px; letter-spacing: 2px; }
  .brand__tag { font-size: 26px; margin-top: 10px; letter-spacing: 1px; }

  .person {
    position: absolute;
    left: 392px;
    top: 92px;
    color: var(--ink);
  }
  .person__name {
    font-family: "Michroma", sans-serif;
    font-size: 23px;
    letter-spacing: 1px;
    white-space: nowrap;
  }
  .person__role {
    font-family: "Cormorant Garamond", serif;
    font-style: italic;
    font-size: 25px;
    color: var(--white);
    margin-left: 120px;
    margin-top: 2px;
  }
  .contact {
    position: absolute;
    left: 392px;
    top: 210px;
    list-style: none;
    font-size: 15px;
    color: var(--ink);
    line-height: 1.2;
  }
  .contact li { display: flex; align-items: flex-start; gap: 8px; margin-bottom: 7px; white-space: nowrap; }
  .contact svg { width: 18px; height: 18px; flex: none; }

  /* Back */
  .back-panel {
    position: absolute;
    left: 0; top: 0; bottom: 0;
    width: 320px;
    background: var(--blue);
  }
  .back-stripe {
    position: absolute;
    right: 0; top: 0; bottom: 0;
    width: 150px;
    background: var(--blue);
  }
  .certs {
    position: absolute;
    left: 32px;
    top: 114px;
    list-style: none;
    color: var(--white);
    font-size: 21px;
    line-height: 1.3;
    white-space: nowrap;
  }
</style>
</head>
<body>
  <section class="card card--front" aria-label="Business card front">
    <svg class="front-disc" viewBox="0 0 700 400" aria-hidden="true">
      <defs>
        <radialGradient id="discFill" cx="0.35" cy="0.3" r="0.8">
          <stop offset="0" stop-color="#7396d6"/>
          <stop offset="1" stop-color="#3d66b0"/>
        </radialGradient>
      </defs>
      <circle cx="640" cy="150" r="295" fill="url(#discFill)"/>
    </svg>

    <div class="brand">
      <div class="brand__name">TRASK</div>
      <div class="brand__tag">AERIAL IMAGING</div>
    </div>

    <div class="person">
      <div class="person__name">DANIEL TRASK</div>
      <div class="person__role">Owner/Operator</div>
    </div>

    <ul class="contact">
      <li>
        <svg viewBox="0 0 18 18" aria-hidden="true"><rect x="5" y="1.5" width="8" height="15" rx="1.5" fill="none" stroke="#fff" stroke-width="1.4"/><line x1="8" y1="14" x2="10" y2="14" stroke="#fff" stroke-width="1.4"/></svg>
        <span>620-555-0187</span>
      </li>
      <li>
        <svg viewBox="0 0 18 18" aria-hidden="true"><rect x="1.5" y="3.5" width="15" height="11" fill="none" stroke="#fff" stroke-width="1.4"/><path d="M1.5 3.5 9 10l7.5-6.5M1.5 14.5l5.5-5M16.5 14.5l-5.5-5" fill="none" stroke="#fff" stroke-width="1.2"/></svg>
        <span>danieltrask@skymail.com</span>
      </li>
      <li>
        <svg viewBox="0 0 18 18" aria-hidden="true"><path d="M9 16.5s-5.5-5.5-5.5-9a5.5 5.5 0 0 1 11 0c0 3.5-5.5 9-5.5 9z" fill="none" stroke="#fff" stroke-width="1.4"/><circle cx="9" cy="7.5" r="2" fill="none" stroke="#fff" stroke-width="1.3"/></svg>
        <span>40528 Birchwood Ct.<br>Calloway Falls KS 67012</span>
      </li>
    </ul>
  </section>

  <section class="card card--back" aria-label="Business card back">
    <div class="back-panel"></div>
    <div class="back-stripe"></div>
    <ul class="certs">
      <li>NAB Drone Certified</li>
      <li>Insured</li>
      <li>Section 333 Exempt</li>
      <li>Vexo Flight Class Certified</li>
    </ul>
  </section>
</body>
</html>
```